Pelorin Conference

We need a pullup banner 23x63 inches. We are attaching an example of a draft that we created. Can you please make it look more professional?
Thank you!

```html
<!DOCTYPE html>
<html lang="en">
<head>
<meta charset="UTF-8">
<title>Pelorin Conference – Pull-up Banners</title>
<link href="https://fonts.googleapis.com/css2?family=Montserrat:wght@500;600;700;800&display=swap" rel="stylesheet">
<style>
  :root {
    --navy: #232d63;
    --orange: #f39c34;
    --sky: #3a8fd0;
    --white: #ffffff;
    --stage: #eef0f3;
    --photo-top: #5fb0e6;
    --photo-mid: #2f6fc0;
    --photo-low: #1b3f8a;
    --field: #3f9a4a;
  }
  * { margin: 0; padding: 0; box-sizing: border-box; }
  html, body {
    width: 983px; height: 1200px; overflow: hidden;
    background: var(--stage);
  }
  .canvas {
    position: relative; width: 983px; height: 1200px;
  }
  .banner {
    position: absolute; top: 124px;
    width: 355px; height: 972px;
    background: var(--white);
  }
  .banner--climate-lines { left: 107px; }
  .banner--services { left: 522px; }
  .banner svg { display: block; width: 355px; height: 972px; }
  .brand-name { font-family: 'Montserrat', sans-serif; font-weight: 800; fill: var(--navy); font-size: 26px; letter-spacing: 0.5px; }
  .headline { font-family: 'Montserrat', sans-serif; font-weight: 700; fill: var(--white); text-anchor: middle; }
  .headline--connector { fill: var(--navy); font-weight: 700; }
  .service { font-family: 'Montserrat', sans-serif; font-weight: 600; fill: var(--white); font-size: 22px; text-anchor: middle; }
  .cta-label { font-family: 'Montserrat', sans-serif; font-weight: 700; fill: var(--white); font-size: 40px; text-anchor: middle; letter-spacing: 1px; }
  .contact-line { font-family: 'Montserrat', sans-serif; font-weight: 600; fill: var(--white); font-size: 24px; text-anchor: middle; }
</style>
</head>
<body>
<main class="canvas">

  <!-- Banner one: weather, climate and catastrophe -->
  <section class="banner banner--climate-lines">
    <svg viewBox="0 0 542 1483" xmlns="http://www.w3.org/2000/svg">
      <defs>
        <linearGradient id="sceneCity" x1="0" y1="0" x2="0" y2="1">
          <stop offset="0" stop-color="var(--photo-top)"/>
          <stop offset="0.45" stop-color="#9fd0ef"/>
          <stop offset="0.6" stop-color="var(--photo-mid)"/>
          <stop offset="1" stop-color="var(--photo-low)"/>
        </linearGradient>
      </defs>

      <g class="brand">
        <rect x="106" y="52" width="56" height="56" fill="var(--orange)"/>
        <text class="brand-name" x="176" y="76">PELORIN</text>
        <text class="brand-name" x="176" y="106">CONFERENCE</text>
      </g>

      <path class="accent-line" d="M0 180 C60 150 140 160 200 250 C260 330 330 300 420 320 C480 335 500 380 542 390" fill="none" stroke="var(--navy)" stroke-width="3"/>

      <path class="hero-photo" role="img" aria-label="City skyline with wind turbines and solar panels under a bright sky with digital network overlay"
            d="M0 300 C80 250 170 250 240 300 C330 360 380 440 480 455 L542 460 L542 860 L0 960 Z" fill="url(#sceneCity)"/>

      <path d="M0 925 C100 885 250 865 330 805 C400 725 460 705 542 795 L542 1483 L0 1483 Z" fill="var(--white)"/>
      <path class="navy-field" d="M0 960 C100 920 250 900 330 840 C400 760 460 740 542 830 L542 1483 L0 1483 Z" fill="var(--navy)"/>

      <text class="headline" x="271" y="1008" font-size="34">SCALING THE MARKET</text>
      <rect x="60" y="1040" width="422" height="38" fill="var(--orange)"/>
      <text class="headline headline--connector" x="271" y="1069" font-size="24">FOR</text>
      <text class="headline" x="271" y="1127" font-size="39">WEATHER, CLIMATE</text>
      <text class="headline" x="271" y="1166" font-size="25">AND NATURAL CATASTROPHE</text>
      <text class="headline" x="271" y="1206" font-size="25">RISK TRANSFER.</text>

      <path d="M0 1300 C150 1270 300 1340 542 1260 L542 1483 L0 1483 Z" fill="var(--white)"/>
      <path class="sky-field" d="M0 1340 C180 1290 330 1390 542 1300 L542 1483 L0 1483 Z" fill="var(--sky)"/>

      <rect class="cta" x="82" y="1280" width="378" height="68" rx="34" fill="var(--orange)"/>
      <text class="cta-label" x="271" y="1329">CONTACT US</text>

      <text class="contact-line" x="271" y="1412">contact@pelorinconference.com</text>
      <text class="contact-line" x="271" y="1449">www.pelorinconference.com</text>
    </svg>
  </section>

  <!-- Banner two: services -->
  <section class="banner banner--services">
    <svg viewBox="0 0 542 1483" xmlns="http://www.w3.org/2000/svg">
      <defs>
        <linearGradient id="sceneField" x1="0" y1="0" x2="0" y2="1">
          <stop offset="0" stop-color="var(--photo-mid)"/>
          <stop offset="0.45" stop-color="var(--photo-top)"/>
          <stop offset="0.62" stop-color="#2c55a8"/>
          <stop offset="0.8" stop-color="#8a7a4a"/>
          <stop offset="1" stop-color="var(--field)"/>
        </linearGradient>
      </defs>

      <g class="brand">
        <rect x="116" y="50" width="56" height="56" fill="var(--orange)"/>
        <text class="brand-name" x="186" y="74">PELORIN</text>
        <text class="brand-name" x="186" y="104">CONFERENCE</text>
      </g>

      <path class="accent-line" d="M0 390 C80 395 100 370 110 300 C130 230 230 215 320 205 C400 195 440 160 480 145 C510 135 530 140 542 150" fill="none" stroke="var(--navy)" stroke-width="3"/>

      <path class="hero-photo" role="img" aria-label="Wind turbines over a solar farm and green field with a digital world map overlay in the sky"
            d="M0 460 C80 450 150 430 190 330 C230 270 300 290 350 260 C400 230 420 180 470 170 L542 180 L542 760 L0 860 Z" fill="url(#sceneField)"/>

      <path d="M0 810 C150 820 250 790 320 740 C400 690 480 710 542 720 L542 1483 L0 1483 Z" fill="var(--white)"/>
      <path class="navy-field" d="M0 840 C150 850 250 820 320 770 C400 720 480 740 542 750 L542 1483 L0 1483 Z" fill="var(--navy)"/>

      <text class="headline" x="271" y="932" font-size="34">SCALING THE MARKET</text>
      <rect x="60" y="952" width="422" height="38" fill="var(--orange)"/>
      <text class="headline headline--connector" x="271" y="981" font-size="24">FOR</text>
      <text class="headline" x="271" y="1033" font-size="29">CLIMATE RISK TRANSFER.</text>

      <g class="service-list">
        <text class="service" x="165" y="1102">Advisory</text>
        <text class="service" x="165" y="1140">Structuring</text>
        <text class="service" x="165" y="1179">Underwriting</text>
        <text class="service" x="405" y="1103">Analytics</text>
        <text class="service" x="405" y="1141">Placement</text>
      </g>

      <path d="M0 1260 C200 1240 350 1300 542 1210 L542 1483 L0 1483 Z" fill="var(--white)"/>
      <path class="sky-field" d="M0 1310 C200 1260 380 1330 542 1240 L542 1483 L0 1483 Z" fill="var(--sky)"/>

      <rect class="cta" x="82" y="1280" width="378" height="68" rx="34" fill="var(--orange)"/>
      <text class="cta-label" x="271" y="1329">CONTACT US</text>

      <text class="contact-line" x="271" y="1412">contact@pelorinconference.com</text>
      <text class="contact-line" x="271" y="1449">www.pelorinconference.com</text>
    </svg>
  </section>

</main>
</body>
</html>
```